** Wanted ** Wordpress web design for scaffolding rental and construction company

We need a website design and must be functional to show a basic overview of what our company offers as a service. We have a domain name and a logo but we need web design. This web site should have another scaffolding rental page for construction and renovation as well as a quote section where customers can enter their personal information and also upload photos. The site% 26quot; www.brixmorvo.com% 26quot; should be intuitive, clear and classy ... The logo must be found on the site in several ways.

Target Market(s)

Professional and no professional

Coding

Coded - Design and coding required

Number of Pages Required

3 page

Font styles to use
Serif
Sans Serif
Decorative
Script

Requirements
Must have
• Our logo
Nice to have
• Slogan:% 26quot; The height% 26 # 224; port% 26 # 233; e hand% 26quot;

```html
<!DOCTYPE html>
<html lang="en">
<head>
<meta charset="utf-8">
<title>Brixmorvo — Scaffolding Rental &amp; Construction</title>
<link href="https://fonts.googleapis.com/css2?family=Michroma&family=Roboto:wght@400;500;700&display=swap" rel="stylesheet">
<style>
:root{
  --orange:#f28a1d;
  --orange-dark:#e0740c;
  --blue:#1896d6;
  --ink:#222;
  --text:#333;
  --muted:#9a9a9a;
  --grey-band:#f4f4f4;
  --navy:#14213a;
  --white:#fff;
}
*{box-sizing:border-box;margin:0;padding:0}
html,body{width:1200px;height:4988px;overflow:hidden}
body{position:relative;background:var(--white);font-family:'Roboto',sans-serif;color:var(--text)}
.abs{position:absolute}
.display{font-family:'Michroma',sans-serif;letter-spacing:2px;font-weight:400}
.accent{color:var(--blue)}

/* hero */
.hero{left:0;top:0;width:1200px;height:832px;background:linear-gradient(160deg,#0f2d6e 0%,#2f5ea8 35%,#8aa1c0 60%,#c9ccd1 80%,#7d8087 100%)}
.hero-shade{left:0;top:0;width:1200px;height:832px;background:linear-gradient(180deg,rgba(5,10,30,.55),rgba(5,10,30,.1) 40%,rgba(0,0,0,0))}
.brand{font-family:'Roboto',sans-serif;font-weight:700;color:var(--orange);letter-spacing:3px;display:flex;align-items:center;gap:10px}
.brand .mark{display:inline-block;background:var(--orange)}
.header-brand{left:145px;top:70px;font-size:28px}
.header-brand .mark{width:18px;height:18px}
.callus{left:745px;top:40px;display:flex;align-items:center;gap:10px;font-weight:700;font-size:21px;color:var(--white)}
.callus b{color:var(--orange)}
.nav{left:455px;top:104px;display:flex;gap:0;font-size:13.5px;font-weight:500;color:var(--white)}
.nav a{color:inherit;text-decoration:none;margin-right:35px;padding-bottom:8px}
.nav a.active{border-bottom:2px solid var(--orange)}
.search{left:1040px;top:106px}
.hero-brand{left:0;top:490px;width:1200px;justify-content:center;font-size:72px;color:var(--white)}
.dots{left:558px;top:661px;display:flex;gap:6px}
.dots span{width:13px;height:13px;border-radius:50%;background:var(--white)}
.dots span.on{background:var(--blue)}
.hero-edge{left:0;top:690px}

/* about */
.about-photo{left:118px;top:842px;width:520px;height:520px;clip-path:polygon(50% 0,100% 50%,50% 100%,0 50%);background:linear-gradient(135deg,#f1efe9,#d9d5cc 55%,#b9b2a6)}
.about-frame{left:112px;top:836px}
.about-title{left:650px;top:900px;font-size:35px;line-height:70px;color:var(--ink)}
.about-copy{left:650px;top:1026px;width:420px;font-size:13.5px;line-height:31.5px;color:var(--muted)}
.btn{background:var(--orange);color:var(--white);font-size:12.5px;font-weight:700;display:flex;align-items:center;justify-content:center;gap:6px}
.about-btn{left:650px;top:1248px;width:140px;height:38px}

/* services */
.service{top:1413px;height:477px}
.service-rental{left:0;width:680px;clip-path:polygon(0 0,551px 0,671px 50%,551px 100%,0 100%);background:linear-gradient(135deg,#f59a3a,#e6791a 60%,#d66a10)}
.service-build{left:610px;width:590px;clip-path:polygon(0 0,100% 0,100% 100%,0 100%,68px 50%);background:linear-gradient(135deg,#7cc6ea,#3d8fc6 50%,#1f5c93)}
.service-label{font-weight:700;font-size:40px;color:var(--white);top:1780px}

/* headings */
.section-title{left:0;width:1200px;text-align:center;font-size:36px;color:var(--ink)}

/* gallery */
.shot{background:linear-gradient(160deg,#9fb7d4,#6b7d93 60%,#3e3d3a)}

/* why */
.why-band{left:0;top:2883px}
.why-photo{left:375px;top:3108px;width:450px;height:450px;clip-path:polygon(50% 0,100% 50%,50% 100%,0 50%);background:linear-gradient(135deg,#f7a24a,#ee8423 55%,#d8690f)}
.why-hole{left:525px;top:3258px;width:150px;height:150px;clip-path:polygon(50% 0,100% 50%,50% 100%,0 50%);background:var(--grey-band)}
.badge{width:80px;height:80px;display:flex;align-items:center;justify-content:center}
.badge::before{content:"";position:absolute;inset:9px;transform:rotate(45deg);background:var(--orange)}
.badge.blue::before{background:var(--blue)}
.badge svg{position:relative}
.feature h3{font-size:21px;font-weight:500;color:var(--ink);margin-bottom:14px}
.feature p{font-size:13px;line-height:21px;color:var(--muted)}
.feature.left{text-align:right;width:260px}
.feature.right{text-align:left;width:285px}

/* news */
.card{top:3899px;width:279px;height:343px;background:var(--white);box-shadow:0 2px 14px rgba(0,0,0,.12)}
.card .thumb{height:163px}
.card .date{position:absolute;left:25px;top:190px;width:46px;height:46px;background:var(--orange);color:var(--white);text-align:center;font-weight:700;font-size:20px;line-height:22px;padding-top:3px}
.card .date small{display:block;font-size:11px;line-height:14px}
.card h4{position:absolute;left:82px;top:188px;font-size:16.5px;font-weight:400;line-height:20px;color:var(--ink)}
.card p{position:absolute;left:25px;top:247px;width:235px;font-size:11px;line-height:17px;color:var(--muted)}
.card .more{position:absolute;left:25px;top:312px;font-size:13px;font-weight:700;color:var(--orange)}

/* footer */
.footer{left:0;top:4315px;width:1200px;height:673px;background:linear-gradient(180deg,#2a3346,#1a2030 50%,#111624)}
.footer-brand{left:0;top:4555px;width:1200px;justify-content:center;font-size:30px}
.footer-brand .mark{width:20px;height:20px}
.foot-head{font-size:15px;font-weight:500;color:var(--white)}
.field{background:var(--white);font-size:10px;color:#777;padding:8px 12px;height:32px}
.submit{left:610px;top:4853px;width:77px;height:27px;border-radius:14px;font-size:11px}
.contact-item{left:757px;display:flex;align-items:center;gap:16px;color:var(--white);font-size:11px;line-height:16px}
.ring{width:34px;height:34px;border-radius:50%;border:1.5px solid #c9c9c9;display:flex;align-items:center;justify-content:center;flex:none}
.rule{left:130px;top:4920px;width:940px;height:1px;background:rgba(255,255,255,.15)}
.copyright{left:130px;top:4951px;font-size:11px;color:var(--white)}
.social{left:893px;top:4943px;display:flex;gap:10px}
.social span{width:24px;height:24px;border-radius:50%}
</style>
</head>
<body>

<!-- HERO -->
<section>
  <div class="abs hero" role="img" aria-label="Aluminium scaffolding and ladders rising against a deep blue sky"></div>
  <div class="abs hero-shade"></div>

  <div class="abs brand header-brand"><span class="mark"></span>BRIXMORVO</div>

  <div class="abs callus">
    <svg width="36" height="36" viewBox="0 0 36 36"><circle cx="18" cy="18" r="16" fill="none" stroke="#1896d6" stroke-width="2.5"/><path d="M13 10c1-1 2-1 3 0l2 3c.5 1 0 2-1 2.5l-1 .5c1 2 2.5 3.5 4.5 4.5l.5-1c.5-1 1.5-1.5 2.5-1l3 2c1 1 1 2 0 3l-1.5 1.5c-4 1-12-7-13-13z" fill="#1896d6"/></svg>
    <span><b>CALL US :</b> 1 555 010 2040</span>
  </div>

  <nav class="abs nav">
    <a class="active" href="#">HOME</a>
    <a href="#">ABOUT US</a>
    <a href="#">SERVICES</a>
    <a href="#">PROJECTS</a>
    <a href="#">NEWS</a>
    <a href="#">CONTACT US</a>
  </nav>
  <svg class="abs search" width="16" height="16" viewBox="0 0 16 16"><circle cx="6.5" cy="6.5" r="4.5" fill="none" stroke="#f28a1d" stroke-width="2"/><path d="M10 10l4 4" stroke="#f28a1d" stroke-width="2.4" stroke-linecap="round"/></svg>

  <div class="abs brand hero-brand">BRIXMORVO</div>

  <div class="abs dots"><span></span><span></span><span class="on"></span><span></span><span></span></div>

  <svg class="abs hero-edge" width="1200" height="150" viewBox="0 0 1200 150">
    <polygon points="0,142 600,30 1200,142 1200,150 0,150" fill="#fff"/>
    <polyline points="0,138 600,28 1200,138" fill="none" stroke="#f28a1d" stroke-width="4"/>
    <polygon points="560,36 600,20 640,36 600,44" fill="#f28a1d"/>
  </svg>
</section>

<!-- ABOUT -->
<section>
  <svg class="abs about-frame" width="532" height="532" viewBox="0 0 532 532"><polygon points="266,3 529,266 266,529 3,266" fill="none" stroke="#f28a1d" stroke-width="4"/></svg>
  <div class="abs about-photo" role="img" aria-label="Architectural plans with a pen on a desk"></div>

  <h2 class="abs display about-title">ABOUT<br><span class="accent">BRIXMORVO</span></h2>
  <p class="abs about-copy">Lorem ipsum dolor sit amet, consectetur adipiscing elied do eiusmod tempor incididunt ut labore et dolore magna aliquis ipsum suspendisse ultrices grorem ipsum dolor si consectetur adipiscing elit, sed do eiusmod tempor incididunt ut labore et dolore magna aliquauis ipsum suspendisse ultrices gravidasus commodo viverra maecenas.</p>
  <div class="abs btn about-btn">READ MORE
    <svg width="12" height="12" viewBox="0 0 12 12"><circle cx="6" cy="6" r="6" fill="#fff"/><path d="M4.5 3l3 3-3 3" stroke="#f28a1d" stroke-width="1.8" fill="none"/></svg>
  </div>
</section>

<!-- SERVICES -->
<section>
  <div class="abs service service-rental" role="img" aria-label="Scaffolding towers silhouetted in orange light"></div>
  <div class="abs service service-build" role="img" aria-label="Engineers in hard hats reviewing plans on a building site"></div>
  <div class="abs service-label" style="left:143px">Scaffolding Rental</div>
  <div class="abs service-label" style="left:790px">Construction</div>
</section>

<!-- PROJECTS GALLERY -->
<section>
  <h2 class="abs display section-title" style="top:2000px">PROJECTS <span class="accent">GALLERY</span></h2>
  <div class="abs shot" style="left:145px;top:2113px;width:527px;height:437px" role="img" aria-label="Worker in hard hat standing on a concrete slab beside a pump boom"></div>
  <div class="abs shot" style="left:683px;top:2113px;width:374px;height:214px;background:linear-gradient(180deg,#3b4a6b,#b87a4a 55%,#e8a24a 75%,#1f1a16)" role="img" aria-label="Workers silhouetted on rebar at sunset"></div>
  <div class="abs shot" style="left:683px;top:2337px;width:374px;height:213px;background:linear-gradient(180deg,#2f6cc2,#5d8fd0 45%,#9a6a48 70%,#5a4a3e)" role="img" aria-label="Scaffolding around a building under blue sky"></div>
  <div class="abs shot" style="left:145px;top:2559px;width:297px;height:214px;background:linear-gradient(180deg,#6c8fc0,#8b96a3 45%,#2f5ea8 75%,#4b4b4b)" role="img" aria-label="Scaffold wrapped building with blue sheeting"></div>
  <div class="abs shot" style="left:451px;top:2559px;width:297px;height:214px;background:linear-gradient(135deg,#8e8b86,#c8c3b9 50%,#d68a2a 70%,#5c5954)" role="img" aria-label="Workers in orange hard hats seen from above"></div>
  <div class="abs shot" style="left:757px;top:2559px;width:300px;height:214px;background:linear-gradient(180deg,#2460b8,#6b8ec4 40%,#8a7666 70%,#4a4038)" role="img" aria-label="Multi-storey scaffolding against blue sky"></div>
</section>

<!-- WHY CHOOSE US -->
<section>
  <svg class="abs why-band" width="1200" height="830" viewBox="0 0 1200 830"><polygon points="0,52 600,0 1200,52 1200,775 600,827 0,775" fill="#f4f4f4"/></svg>
  <h2 class="abs display section-title" style="top:3015px">WHY &nbsp;<span class="accent">CHOOSE US</span></h2>

  <div class="abs why-photo" role="img" aria-label="Scaffolding and crane in orange tones"></div>
  <div class="abs why-hole"></div>

  <div class="abs badge" style="left:415px;top:3138px"><svg width="26" height="26" viewBox="0 0 26 26"><rect x="3" y="5" width="20" height="17" fill="none" stroke="#fff" stroke-width="2"/><path d="M3 10h20M8 3v4M18 3v4" stroke="#fff" stroke-width="2"/></svg></div>
  <div class="abs badge blue" style="left:690px;top:3138px"><svg width="26" height="26" viewBox="0 0 26 26"><rect x="5" y="6" width="16" height="16" fill="none" stroke="#fff" stroke-width="2"/><path d="M9 10h3M14 10h3M9 14h3M14 14h3M11 22v-4h4v4" stroke="#fff" stroke-width="1.8"/></svg></div>
  <div class="abs badge blue" style="left:415px;top:3453px"><svg width="26" height="26" viewBox="0 0 26 26"><path d="M8 23V5M4 5h18M8 9l4-4M20 5v6" stroke="#fff" stroke-width="2" fill="none"/><rect x="17" y="11" width="6" height="4" fill="#fff"/></svg></div>
  <div class="abs badge" style="left:690px;top:3453px"><svg width="26" height="26" viewBox="0 0 26 26"><path d="M6 12a7 7 0 0 1 14 0z" fill="#fff"/><rect x="5" y="12" width="16" height="2" fill="#fff"/><path d="M6 23c0-4 3-6 7-6s7 2 7 6" fill="none" stroke="#fff" stroke-width="2"/></svg></div>

  <div class="abs feature left" style="left:133px;top:3138px"><h3>20 YEARS EXPERIENCE</h3><p>Lorem ipsum dolor sit amet, consectetur adipiscing elit, sed do eiusmod tempor incididunt ut labore et dolore magna</p></div>
  <div class="abs feature right" style="left:807px;top:3138px"><h3>MORE THAN 200 PROJECTS</h3><p>Lorem ipsum dolor sit amet, consectetur adipiscing elit, sed do eiusmod tempor incididunt ut labore et dolore magna</p></div>
  <div class="abs feature left" style="left:133px;top:3452px"><h3>UNIQUE CONSTRUCTION</h3><p>Lorem ipsum dolor sit amet, consectetur adipiscing elit, sed do eiusmod tempor incididunt ut labore et dolore magna</p></div>
  <div class="abs feature right" style="left:807px;top:3452px"><h3>TOPER BUILDERS</h3><p>Lorem ipsum dolor sit amet, consectetur adipiscing elit, sed do eiusmod tempor incididunt ut labore et dolore magna</p></div>
</section>

<!-- LATEST NEWS -->
<section>
  <h2 class="abs display section-title" style="top:3806px">LATEST <span class="accent">NEWS</span></h2>

  <article class="abs card" style="left:155px">
    <div class="thumb" style="background:linear-gradient(160deg,#d8d6d2,#9ea6b0 50%,#6a6f78)" role="img" aria-label="Workers assembling scaffolding"></div>
    <div class="date">02<small>JAN</small></div>
    <h4>Pellentesque faucibus<br>Ut accumsan ultric</h4>
    <p>Duis quam Nam eget lacus Aliquam erat volutpat Quisque dignissim congue leo Mauris vel lacus vitae felis vestibulum</p>
    <div class="more">READ MORE</div>
  </article>
  <article class="abs card" style="left:461px">
    <div class="thumb" style="background:linear-gradient(180deg,#3f78c6,#8aa9d4 40%,#c2b04a 70%,#6b6440)" role="img" aria-label="Building wrapped in yellow scaffolding"></div>
    <div class="date">02<small>JAN</small></div>
    <h4>Pellentesque faucibus<br>Ut accumsan ultric</h4>
    <p>Duis quam Nam eget lacus Aliquam erat volutpat Quisque dignissim congue leo Mauris vel lacus vitae felis vestibulum</p>
    <div class="more">READ MORE</div>
  </article>
  <article class="abs card" style="left:767px">
    <div class="thumb" style="background:linear-gradient(135deg,#f3f1ec,#d7d2c8 60%,#a89f91)" role="img" aria-label="Pen resting on building plans"></div>
    <div class="date">02<small>JAN</small></div>
    <h4>Pellentesque faucibus<br>Ut accumsan ultric</h4>
    <p>Duis quam Nam eget lacus Aliquam erat volutpat Quisque dignissim congue leo Mauris vel lacus vitae felis vestibulum</p>
    <div class="more">READ MORE</div>
  </article>
</section>

<!-- FOOTER -->
<footer>
  <div class="abs footer" role="img" aria-label="Construction site with crane at dusk"></div>
  <svg class="abs" style="left:0;top:4315px" width="1200" height="130" viewBox="0 0 1200 130">
    <polygon points="0,0 1200,0 1200,2 600,116 0,2" fill="#fff"/>
    <polyline points="0,4 600,118 1200,4" fill="none" stroke="#f28a1d" stroke-width="4"/>
    <polygon points="565,104 600,124 635,104 600,112" fill="#f28a1d"/>
  </svg>

  <div class="abs brand footer-brand"><span class="mark"></span>BRIXMORVO</div>

  <div class="abs foot-head" style="left:145px;top:4630px">Get In Touch:</div>
  <div class="abs field" style="left:145px;top:4666px;width:265px">NAME</div>
  <div class="abs field" style="left:422px;top:4666px;width:265px">PHONE</div>
  <div class="abs field" style="left:145px;top:4708px;width:542px">UPLOAD PHOTOS</div>
  <svg class="abs" style="left:660px;top:4714px" width="20" height="20" viewBox="0 0 20 20"><circle cx="10" cy="10" r="9" fill="#f28a1d"/><path d="M10 14V6M7 9l3-3 3 3" stroke="#fff" stroke-width="1.8" fill="none"/></svg>
  <div class="abs field" style="left:145px;top:4750px;width:542px;height:70px">MESSAGE :</div>
  <div class="abs btn submit">SUBMIT</div>

  <div class="abs foot-head" style="left:757px;top:4630px">Contact Information</div>
  <div class="abs contact-item" style="top:4673px">
    <span class="ring"><svg width="14" height="16" viewBox="0 0 14 16"><path d="M7 15s5-5 5-9A5 5 0 0 0 2 6c0 4 5 9 5 9z" fill="none" stroke="#f28a1d" stroke-width="1.8"/><circle cx="7" cy="6" r="1.8" fill="#f28a1d"/></svg></span>
    <span>323,Sed ut perspiciatis unde omnis iste<br>natus error ccusantium.</span>
  </div>
  <div class="abs contact-item" style="top:4722px">
    <span class="ring"><svg width="14" height="14" viewBox="0 0 14 14"><path d="M3 1c1-1 2 0 2.5 1l1 2c.3.8-.2 1.4-.8 1.8.8 1.6 1.8 2.6 3.4 3.4.4-.6 1-1.1 1.8-.8l2 1c1 .5 2 1.5 1 2.5-2 2-11-7-10.9-10.9z" fill="#f28a1d"/></svg></span>
    <span>Phone : 1 555 010 2040</span>
  </div>
  <div class="abs contact-item" style="top:4765px">
    <span class="ring"><svg width="14" height="11" viewBox="0 0 14 11"><rect x="1" y="1" width="12" height="9" fill="#f28a1d"/><path d="M1 1l6 5 6-5" stroke="#fff" stroke-width="1.2" fill="none"/></svg></span>
    <span>Email : info@brixmorvo.com</span>
  </div>
  <div class="abs contact-item" style="top:4812px;font-size:15px;font-weight:700">
    <span class="ring"><svg width="16" height="16" viewBox="0 0 16 16"><circle cx="8" cy="8" r="6.5" fill="none" stroke="#f28a1d" stroke-width="1.8"/><path d="M8 4v4l3 2" stroke="#f28a1d" stroke-width="1.8" fill="none"/></svg></span>
    <span>24/7</span>
  </div>

  <div class="abs rule"></div>
  <div class="abs copyright">Copyrights © 2020 Brixmorvo.All Rights Reserved. &nbsp;| &nbsp;Privacy policy</div>
  <div class="abs social"><span style="background:#3b5998"></span><span style="background:#1da1f2"></span><span style="background:#e52d27"></span><span style="background:#c1914f"></span><span style="background:#0e76a8"></span></div>
</footer>

</body>
</html>
```